Corkbell Cellars: the premier wine registry - (need business cards)

We have a logo designed, and now we need business cards for our 3 founders. Corkbell Cellars is the premier wine registry for weddings. I am envisioning the wine glass with the heart in it as our signature symbol. (FYI- on the red background file, only use the part that has the red background; the brown colors are not relevant)

```html
<!DOCTYPE html>
<html lang="en">
<head>
<meta charset="utf-8">
<title>Corkbell Cellars — Business Cards</title>
<link href="https://fonts.googleapis.com/css2?family=Arimo:wght@400;700&display=swap" rel="stylesheet">
<style>
  :root {
    --backdrop: #e4e4e6;
    --wine: #a01f4f;
    --wine-deep: #5e1830;
    --paper: #ffffff;
    --ink-grey: #6f6f73;
    --ink-dark: #555558;
    --shadow: rgba(0, 0, 0, 0.18);
  }
  * { margin: 0; padding: 0; box-sizing: border-box; }
  html, body {
    width: 1200px;
    height: 900px;
    overflow: hidden;
    background: var(--backdrop);
    font-family: "Arimo", Arial, sans-serif;
  }
  .sheet {
    width: 1200px;
    height: 900px;
    display: flex;
    align-items: center;
    justify-content: center;
    gap: 40px;
  }
  .card {
    position: relative;
    width: 540px;
    height: 309px;
    border-radius: 3px;
    overflow: hidden;
    box-shadow: 0 14px 30px var(--shadow);
  }

  /* Front */
  .card-front { background: var(--wine); }
  .card-front .wine-splash {
    position: absolute;
    right: 0;
    top: 0;
    width: 260px;
    height: 309px;
  }
  .card-front .brand {
    position: absolute;
    left: 92px;
    top: 160px;
    display: flex;
    align-items: center;
    gap: 12px;
  }
  .brand-dot {
    width: 16px;
    height: 16px;
    border-radius: 50%;
    flex: none;
  }
  .card-front .brand-dot { background: #ffffff; }
  .brand-name {
    font-weight: 400;
    letter-spacing: 0.32em;
    text-transform: uppercase;
    white-space: nowrap;
  }
  .card-front .brand-name { color: #ffffff; font-size: 22px; }

  /* Back */
  .card-back { background: var(--paper); }
  .card-back .brand {
    position: absolute;
    left: 38px;
    top: 46px;
    display: flex;
    align-items: center;
    gap: 9px;
  }
  .card-back .brand-dot { background: var(--wine); width: 12px; height: 12px; }
  .card-back .brand-name { color: var(--wine); font-size: 15px; }

  .person {
    position: absolute;
    left: 38px;
    top: 118px;
  }
  .person-name {
    color: var(--wine);
    font-weight: 700;
    font-size: 34px;
    letter-spacing: -0.02em;
    line-height: 1;
  }
  .person-role {
    color: var(--ink-dark);
    font-weight: 700;
    font-size: 15px;
    margin-top: 4px;
  }
  .address {
    position: absolute;
    left: 38px;
    top: 196px;
    color: var(--ink-grey);
    font-size: 13.5px;
    line-height: 1.45;
    font-style: normal;
  }
  .contacts {
    position: absolute;
    left: 300px;
    top: 196px;
    list-style: none;
    color: var(--ink-grey);
    font-size: 12.5px;
    line-height: 1.5;
  }
</style>
</head>
<body>
  <main class="sheet">
    <section class="card card-front" aria-label="Business card front">
      <svg class="wine-splash" viewBox="0 0 260 309" role="img" aria-label="Abstract swirl of poured red wine in deep burgundy tones">
        <defs>
          <linearGradient id="splashFill" x1="0" y1="0" x2="1" y2="1">
            <stop offset="0" stop-color="#6e1a33"/>
            <stop offset="0.6" stop-color="#5a1a2e"/>
            <stop offset="1" stop-color="#3e1c2c"/>
          </linearGradient>
        </defs>
        <path d="M60 0 H260 V309 H150 C90 300 40 250 38 180 C36 110 20 50 60 0 Z" fill="url(#splashFill)" opacity="0.92"/>
      </svg>
      <div class="brand">
        <span class="brand-dot"></span>
        <span class="brand-name">Corkbell Cellars</span>
      </div>
    </section>

    <section class="card card-back" aria-label="Business card back">
      <div class="brand">
        <span class="brand-dot"></span>
        <span class="brand-name">Corkbell Cellars</span>
      </div>
      <div class="person">
        <p class="person-name">Mara Quill</p>
        <p class="person-role">Director</p>
      </div>
      <address class="address">
        Corkbell Cellars. Co<br>
        48, Alder Lane,<br>
        Reno nevada
      </address>
      <ul class="contacts">
        <li>M. +1-555-204-7731</li>
        <li>T. +1-555-204-7731</li>
        <li>E. mara@corkbellcellars.com</li>
      </ul>
    </section>
  </main>
</body>
</html>
```